A taxi bidding business needs Web Design

We need a cutting edge, super UX-intuitive, Elegant web design for our business called Rydello.

Rydello is Australia based Kind of "Next Zenvo" business where user creates a trip and cabs/drivers place bids on fares/bookings/trips and lowest bidder gets the job.
User can also share the Cabs going in same route to get lowest bids.

- The design needs to be very, very intuitive to use and navigate. Please do not use much of yellow color.

References: StayKoro & Zenvo

Please see the attached pdf, attaching logo as well.

Target Market(s)

Ride Sharing, Taxi

Industry/Entity Type

Business

Number of Pages Required

5+ page

Requirements
Must have
• Icons/graphics, How it works icons, case studies icons, all mentioned pages
Should not have
• Not much yellow color

```html
<!DOCTYPE html>
<html lang="en">
<head>
<meta charset="utf-8">
<title>Rydello – A reliable way to travel</title>
<link rel="stylesheet" href="https://fonts.googleapis.com/css2?family=Montserrat:wght@400;500;600;700&family=Open+Sans:wght@400;600&display=swap">
<style>
:root{
  --red:#e31b23;
  --ink:#2b2b2b;
  --muted:#6d6d6d;
  --line:#e6e6e6;
  --white:#ffffff;
  --footer:#262626;
  --footer-edge:#333333;
  --footer-deep:#1c1c1c;
}
*{box-sizing:border-box;margin:0;padding:0}
html,body{width:1200px;height:2314px;overflow:hidden;background:var(--white)}
body{position:relative;font-family:"Open Sans",Arial,sans-serif;color:var(--ink)}

/* header */
.site-header{position:absolute;top:0;left:0;width:1200px;height:57px;background:var(--white);border-bottom:1px solid var(--line);z-index:3}
.brand{position:absolute;left:89px;top:10px;display:flex;align-items:center;gap:6px;font-family:"Montserrat",sans-serif;font-weight:700;font-size:14px;color:var(--ink);letter-spacing:.5px}
.brand-dot{width:12px;height:12px;border-radius:50%;background:var(--red)}
.main-nav{position:absolute;left:260px;top:0;height:57px;display:flex}
.main-nav a{display:flex;align-items:center;gap:7px;height:57px;padding:0 20px;border-left:1px solid var(--line);font-size:12px;color:#444;text-decoration:none}
.main-nav a:last-child{border-right:1px solid var(--line)}
.main-nav svg{width:12px;height:12px;fill:#444}
.account{position:absolute;right:110px;top:0;height:57px;display:flex;align-items:center;gap:7px;font-size:12px;color:#444}
.account svg{width:11px;height:11px;fill:#444}
.menu-toggle{position:absolute;right:70px;top:0;height:57px;display:flex;flex-direction:column;justify-content:center;gap:3px}
.menu-toggle span{display:block;width:18px;height:2px;background:#333}

/* hero */
.hero{position:absolute;top:57px;left:0;width:1200px;height:441px;background:linear-gradient(90deg,#2c3440 0%,#3d4450 35%,#5a4a63 62%,#6b3f78 80%,#5c4a5a 100%)}
.photo{width:100%;height:100%}
.hero-shade{position:absolute;inset:0;background:linear-gradient(90deg,rgba(0,0,0,.35),rgba(0,0,0,0) 55%)}
.hero-copy{position:absolute;left:120px;top:128px;color:var(--white)}
.hero-kicker{font-family:"Montserrat",sans-serif;font-size:17px;font-weight:400}
.hero-title{margin-top:14px;font-family:"Montserrat",sans-serif;font-weight:700;font-size:39px;line-height:52px;text-transform:uppercase;letter-spacing:.3px}
.btn-primary{display:inline-flex;align-items:center;justify-content:center;margin-top:22px;width:199px;height:43px;background:var(--red);color:var(--white);font-size:14px;font-weight:600}

/* feature grid */
.features{position:absolute;top:452px;left:85px;width:1027px;height:1398px;display:grid;grid-template-columns:repeat(3,1fr);grid-template-rows:repeat(6,233px);border:1px solid var(--line);background:var(--white)}
.tile{position:relative}
.notch::after{content:"";position:absolute;width:0;height:0;border:11px solid transparent;z-index:2}
.notch-bottom::after{left:16px;bottom:0;border-bottom-color:var(--white)}
.notch-top::after{left:16px;top:-22px;border-bottom-color:var(--white)}
.notch-right::after{right:0;top:28px;border-right-color:var(--white)}
.tile-text{padding:44px 26px 0 19px}
.tile-text.lower{padding-top:70px}
.tile-title{font-family:"Montserrat",sans-serif;font-weight:500;font-size:15.5px;color:#333;margin-bottom:6px}
.tile-body{font-size:12px;line-height:20.5px;color:var(--muted)}
.tile-feature{background:var(--red);color:var(--white);padding:141px 20px 0 21px}
.tile-feature .tile-title,.tile-feature .tile-body{color:var(--white)}
.tile-feature .tile-body{font-weight:600}
.btn-light{display:inline-flex;align-items:center;justify-content:center;margin-top:24px;width:138px;height:40px;background:var(--white);color:#333;font-size:13px;font-weight:600}
.feature-photo{position:absolute;left:14px;bottom:6px;width:196px;height:74px;background:linear-gradient(180deg,rgba(240,190,50,.85),rgba(210,150,30,.85))}

.c1{grid-column:1}.c2{grid-column:2}.c3{grid-column:3}
.r1{grid-row:1}.r2{grid-row:2}.r3{grid-row:3}.r4{grid-row:4}.r5{grid-row:5}.r6{grid-row:6}
.r34{grid-row:3 / span 2}

/* footer */
.site-footer{position:absolute;top:1890px;left:0;width:1200px;height:424px}
.footer-edge{position:absolute;top:0;left:0;width:1200px;height:200px}
.footer-map{position:absolute;top:200px;left:0;width:1200px;height:162px;background:var(--footer)}
.footer-cols{position:absolute;top:165px;left:0;width:1200px;height:200px}
.footer-col{position:absolute;top:0;color:var(--white)}
.footer-col h3{font-family:"Montserrat",sans-serif;font-weight:500;font-size:19px;margin-bottom:14px}
.footer-col ul{list-style:none}
.footer-col li{font-size:12px;line-height:31px}
.col-links{left:227px}
.col-cities{left:523px}
.col-follow{left:814px}
.social{display:flex;gap:16px;margin:6px 0 30px}
.social span{width:13px;height:13px;border-radius:50%;background:var(--white)}
.apps-title{font-family:"Montserrat",sans-serif;font-weight:600;font-size:13px;margin-bottom:12px}
.stores{display:flex;gap:19px}
.stores span{width:103px;height:33px;border-radius:5px;background:#000;border:1px solid #8a8a8a}
.footer-bar{position:absolute;bottom:0;left:0;width:1200px;height:62px;background:var(--footer-deep);color:var(--white);font-size:11px}
.footer-bar .copy{position:absolute;left:227px;top:24px}
.footer-bar .rights{position:absolute;right:154px;top:24px}
</style>
</head>
<body>

<header class="site-header">
  <div class="brand"><span class="brand-dot"></span>RYDELLO</div>
  <nav class="main-nav">
    <a href="#"><svg viewBox="0 0 12 12"><path d="M2 5l1.5-3h5L10 5h1v4H10v1.5H8.5V9h-5v1.5H2V9H1V5z"/></svg>Ride</a>
    <a href="#"><svg viewBox="0 0 12 12"><circle cx="6" cy="6" r="5" fill="none" stroke="#444" stroke-width="1.6"/><circle cx="6" cy="6" r="1.5"/></svg>Drive</a>
  </nav>
  <div class="account"><svg viewBox="0 0 12 12"><circle cx="6" cy="3.5" r="2.8"/><path d="M1 12c0-3 2.2-5 5-5s5 2 5 5z"/></svg>Sign In</div>
  <div class="menu-toggle"><span></span><span></span><span></span></div>
</header>

<section class="hero">
  <div class="photo" role="img" aria-label="Woman in a purple coat booking a ride on her phone beside a taxi rank"></div>
  <div class="hero-shade"></div>
  <div class="hero-copy">
    <p class="hero-kicker">Book a car</p>
    <h1 class="hero-title">A reliable way to<br>travel</h1>
    <a class="btn-primary">Search Now</a>
  </div>
</section>

<section class="features">
  <div class="tile c1 r1 notch notch-bottom"><div class="photo" role="img" aria-label="Smiling passengers looking out of a yellow taxi window" style="background:linear-gradient(135deg,#c9b07a,#8a6a4c 50%,#e0b93a)"></div></div>
  <div class="tile c2 r1 tile-text lower"><h2 class="tile-title">Automated Bidding, Saves Times</h2><p class="tile-body">Mauris posuere mi id felis lobortis maximus. Nunc ac dui iaculis, facilisis eros vitae, hendrerit nulla. Vivamus nisl tellus, mollis eu elit in, suscipit venenatis quam. Duis et feugiat enim.</p></div>
  <div class="tile c3 r1 notch notch-bottom"><div class="photo" role="img" aria-label="White taxi on a city street with trees" style="background:linear-gradient(180deg,#9a9a86,#7f8a70 55%,#c9c9c4)"></div></div>

  <div class="tile c1 r2 tile-text"><h2 class="tile-title">Instant Bids, Slashed fares</h2><p class="tile-body">Mauris posuere mi id felis lobortis maximus. Nunc ac dui iaculis, facilisis eros vitae, hendrerit nulla. Vivamus nisl tellus, mollis eu elit in, suscipit venenatis quam. Duis et feugiat enim.</p></div>
  <div class="tile c2 r2 notch notch-top"><div class="photo" role="img" aria-label="Businessman checking his phone while hailing a cab" style="background:linear-gradient(135deg,#8b8a82,#55595e 50%,#9aa38c)"></div></div>
  <div class="tile c3 r2 tile-text"><h2 class="tile-title">Speedy Services Anywhere Anytime</h2><p class="tile-body">Mauris posuere mi id felis lobortis maximus. Nunc ac dui iaculis, facilisis eros vitae, hendrerit nulla. Vivamus nisl tellus, mollis eu elit in, suscipit venenatis quam. Duis et feugiat enim.</p></div>

  <div class="tile c1 r34 notch notch-right"><div class="photo" role="img" aria-label="Woman with shopping bags stepping out of a yellow taxi" style="background:linear-gradient(160deg,#b9a58a,#b4563a 45%,#d9a526 80%,#5a5048)"></div></div>
  <div class="tile c2 r34 tile-feature">
    <h2 class="tile-title">Multiple Hiring , Huge Discounts</h2>
    <p class="tile-body">Mauris posuere mi id felis lobortis maximus. Nunc ac dui iaculis, facilisis eros vitae, hendrerit nulla. Vivamus nisl tellus, mollis eu elit in, suscipit venenatis quam. Duis et feugiat enim.</p>
    <a class="btn-light">Read More</a>
    <div class="feature-photo" role="img" aria-label="Photo of a yellow taxi van"></div>
  </div>
  <div class="tile c3 r3 notch notch-bottom"><div class="photo" role="img" aria-label="White stretch limousine parked on a street" style="background:linear-gradient(180deg,#6f7a68,#d8d8d6 55%,#55565a)"></div></div>
  <div class="tile c3 r4 tile-text"><h2 class="tile-title">Luxury Hires</h2><p class="tile-body">Mauris posuere mi id felis lobortis maximus. Nunc ac dui iaculis, facilisis eros vitae, hendrerit nulla. Vivamus nisl tellus, mollis eu elit in, suscipit venenatis quam. Duis et feugiat enim.</p></div>

  <div class="tile c1 r5 notch notch-bottom"><div class="photo" role="img" aria-label="Couple riding in the back of a yellow taxi" style="background:linear-gradient(135deg,#e1b62c,#a5603f 55%,#c9a98b)"></div></div>
  <div class="tile c2 r5 tile-text"><h2 class="tile-title">Safe Traval</h2><p class="tile-body">Mauris posuere mi id felis lobortis maximus. Nunc ac dui iaculis, facilisis eros vitae, hendrerit nulla. Vivamus nisl tellus, mollis eu elit in, suscipit venenatis quam. Duis et feugiat enim.</p></div>
  <div class="tile c3 r5"><div class="photo" role="img" aria-label="Woman in a purple coat using her phone near parked taxis" style="background:linear-gradient(120deg,#3d4450,#5a5f6a 45%,#7a3f86 80%)"></div></div>

  <div class="tile c1 r6 tile-text"><h2 class="tile-title">Save Smart</h2><p class="tile-body">Mauris posuere mi id felis lobortis maximus. Nunc ac dui iaculis, facilisis eros vitae, hendrerit nulla. Vivamus nisl tellus, mollis eu elit in, suscipit venenatis quam. Duis et feugiat enim.</p></div>
  <div class="tile c2 r6 notch notch-top"><div class="photo" role="img" aria-label="Passenger with a bag getting into a red taxi" style="background:linear-gradient(135deg,#6d6660,#b8262c 50%,#8a1d22)"></div></div>
  <div class="tile c3 r6 tile-text"><h2 class="tile-title">Speedy Services Anywhere Anytime</h2><p class="tile-body">Mauris posuere mi id felis lobortis maximus. Nunc ac dui iaculis, facilisis eros vitae, hendrerit nulla. Vivamus nisl tellus, mollis eu elit in, suscipit venenatis quam. Duis et feugiat enim.</p></div>
</section>

<footer class="site-footer">
  <svg class="footer-edge" viewBox="0 0 1200 200" preserveAspectRatio="none" role="img" aria-label="Winding road illustration with a small taxi">
    <path d="M0 80 C150 30 300 0 450 8 C650 20 780 100 950 110 C1060 116 1140 108 1200 110 L1200 200 L0 200Z" fill="var(--footer)"/>
  </svg>
  <div class="footer-map" role="img" aria-label="Faint map of Australia"></div>
  <div class="footer-cols">
    <div class="footer-col col-links"><h3>Usefull link</h3><ul><li>Ride</li><li>Drive</li><li>Cities</li><li>Fare Estimate</li><li>How It Works</li></ul></div>
    <div class="footer-col col-cities"><h3>Top Cities</h3><ul><li>San Francisco</li><li>London</li><li>Los Angeles</li><li>Washington D.C.</li><li>Mexico City</li></ul></div>
    <div class="footer-col col-follow"><h3>Follow Us</h3>
      <div class="social"><span></span><span></span><span></span><span></span></div>
      <p class="apps-title">Download Rydello Apps</p>
      <div class="stores"><span></span><span></span></div>
    </div>
  </div>
  <div class="footer-bar"><span class="copy">© 2017 Rydello.</span><span class="rights">All Rights Reserved</span></div>
</footer>

</body>
</html>
```